Recommend a friend FLYER - Brisk Window Cleaning

Window cleaning company with focus on quality of service and professionalism. Friendly, relaxed tone, and simple clear communications.

Target Market(s)

Homeowners with moderate income

Industry/Entity Type

Window Cleaning

Font styles to use
Serif
Decorative

Colors
33a6d7
fbee3d
faa54b
d3d3d3

```html
<!DOCTYPE html>
<html lang="en">
<head>
<meta charset="utf-8">
<title>Recommend a Friend – Brisk Window Cleaning</title>
<link rel="stylesheet" href="https://fonts.googleapis.com/css2?family=Libre+Baskerville:ital,wght@0,700;1,700&display=swap">
<style>
  :root {
    --sky: #00a6de;
    --navy: #1f3f8c;
    --white: #ffffff;
    --thanks-blue: #1ea3dc;
    --trim-red: #e8646a;
    --trim-blue: #3ab0e0;
    --mascot-light: #e6f5fb;
    --mascot-mid: #a9dbf0;
    --accent-orange: #faa54b;
    --accent-yellow: #fbee3d;
    --shadow-grey: #d3d3d3;
  }
  * { margin: 0; padding: 0; box-sizing: border-box; }
  html, body { width: 851px; height: 1200px; overflow: hidden; background: var(--white); }
  .flyer {
    position: relative;
    width: 851px;
    height: 1200px;
    overflow: hidden;
    background: var(--white);
    font-family: "Libre Baskerville", Georgia, serif;
  }
  .trim-outer {
    position: absolute; inset: 2px;
    border: 1px solid var(--trim-red);
    pointer-events: none; z-index: 5;
  }
  .trim-inner {
    position: absolute; inset: 14px;
    border: 1px solid var(--trim-blue);
    pointer-events: none; z-index: 5;
  }
  .header-wave {
    position: absolute; top: 0; left: 0;
    width: 851px; height: 600px;
  }
  .offer {
    position: absolute; top: 46px; left: 0; right: 0;
    color: var(--white);
    text-align: center;
    font-weight: 700;
    font-size: 36px;
    line-height: 48px;
    letter-spacing: 1.4px;
    white-space: nowrap;
  }
  .offer p + p { margin-top: 49px; }
  .mascot {
    position: absolute;
    left: 81px; top: 552px;
    width: 500px; height: 406px;
    border-radius: 40px;
    background:
      radial-gradient(ellipse 60% 45% at 50% 100%, rgba(250, 165, 75, 0.45) 0%, rgba(251, 238, 61, 0.2) 55%, rgba(255, 255, 255, 0) 100%),
      linear-gradient(180deg, var(--white) 0%, var(--mascot-light) 35%, var(--mascot-mid) 75%, var(--mascot-light) 100%);
  }
  .thanks {
    position: absolute; top: 964px; left: 0; right: 0;
    text-align: center;
    color: var(--thanks-blue);
    font-style: italic;
    font-weight: 700;
    font-size: 56px;
    line-height: 55px;
    letter-spacing: 0.5px;
  }
  .brand {
    position: absolute; top: 1104px; left: 0; right: 0;
    display: flex; justify-content: center; align-items: center; gap: 12px;
  }
  .brand-name {
    color: var(--navy);
    font-weight: 700;
    font-size: 32px;
  }
  .brand-mark {
    width: 28px; height: 28px;
    background: var(--sky);
  }
</style>
</head>
<body>
  <main class="flyer">
    <div class="trim-outer"></div>
    <div class="trim-inner"></div>

    <svg class="header-wave" viewBox="0 0 851 600" aria-hidden="true">
      <path d="M0 0 H851 V465 Q425 644 0 430 Z" fill="var(--navy)"/>
      <path d="M0 0 H851 V440 Q425 630 0 420 Z" fill="var(--sky)"/>
    </svg>

    <section class="offer">
      <p>You will receive a £10 voucher<br>redeemable against any of our<br>services, on completion of your<br>friend’s first clean. Must be within<br>the areas we cover.</p>
      <p>You will receive a voucher for each<br>referral. Recommend us to as many<br>friends as you can!</p>
    </section>

    <div class="mascot" role="img" aria-label="Illustration of a cheerful blue bird mascot with an orange beak and feet, shouting through a red and white megaphone"></div>

    <h2 class="thanks">Thank you for your<br>loyal support</h2>

    <footer class="brand">
      <span class="brand-name">Brisk Window Cleaning</span>
      <span class="brand-mark"></span>
    </footer>
  </main>
</body>
</html>
```